High End Mechanic Business Card Design Project

Automotive Business - Repair, service and sales
Bold background with clarity of text

Industry/Entity Type

Automotive

Contact Information for Business Card

Black background with silver or white kvt 418 lorne coupe at the bottom right angered with the business name and address at the top left.. Also to include a compass near the business name and the text... Sales Service RepairAdded photos as EXAMPLES. Don't want the actual n, s, e w on the compass picture but to know that it is a compass.

Font styles to use
Sans Serif

Requirements
Must have
• Creativity, black background, Images: 4 Lorne KVT Coupe & Compass (without text)

```html
<!DOCTYPE html>
<html lang="en">
<head>
<meta charset="utf-8">
<title>Harlow Ridge Motors – Business Card</title>
<link href="https://fonts.googleapis.com/css2?family=Exo+2:wght@700&family=Cousine&family=Montserrat:wght@800&display=swap" rel="stylesheet">
<style>
  :root {
    --page-bg: #e9ecec;
    --card-black: #000000;
    --text-white: #ffffff;
    --icon-grey: #3a3a3a;
    --silver-light: #d9d9d9;
    --silver-mid: #9a9a9a;
    --silver-dark: #4a4a4a;
  }
  html, body {
    margin: 0;
    width: 1200px;
    height: 900px;
    overflow: hidden;
    background: var(--page-bg);
  }
  .business-card {
    position: absolute;
    left: 150px;
    top: 193px;
    width: 900px;
    height: 514px;
    background: var(--card-black);
    overflow: hidden;
    color: var(--text-white);
    box-shadow: 0 8px 24px rgba(0,0,0,0.18);
  }
  .company-name {
    position: absolute;
    left: 62px;
    top: 34px;
    margin: 0;
    font-family: "Exo 2", sans-serif;
    font-weight: 700;
    font-size: 58px;
    letter-spacing: 1px;
    line-height: 1;
  }
  .contact-list {
    position: absolute;
    left: 88px;
    top: 120px;
    margin: 0;
    padding: 0;
    list-style: none;
    font-family: "Cousine", monospace;
    font-size: 25px;
    line-height: 32px;
  }
  .contact-item {
    display: flex;
    align-items: flex-start;
    gap: 14px;
    margin-bottom: 14px;
  }
  .contact-item.phone { align-items: center; }
  .contact-text span { display: block; }
  .contact-icon {
    flex: 0 0 38px;
    width: 38px;
    height: 38px;
    border-radius: 50%;
    background: var(--icon-grey);
    display: flex;
    align-items: center;
    justify-content: center;
  }
  .contact-item.address .contact-icon { margin-top: 13px; }
  .compass-art {
    position: absolute;
    left: 100px;
    top: 300px;
    width: 250px;
    height: 250px;
    border-radius: 50%;
    background: radial-gradient(circle, var(--silver-light) 0%, var(--silver-mid) 35%, var(--silver-dark) 60%, var(--card-black) 72%);
  }
  .car-photo {
    position: absolute;
    right: 0;
    top: 128px;
    width: 180px;
    height: 145px;
    border-radius: 70px 0 0 20px;
    background: linear-gradient(160deg, var(--silver-light) 0%, var(--silver-mid) 55%, var(--silver-dark) 100%);
  }
  .services-tagline {
    position: absolute;
    right: 28px;
    top: 412px;
    margin: 0;
    font-family: "Montserrat", sans-serif;
    font-weight: 800;
    font-size: 36px;
    letter-spacing: 0.5px;
  }
</style>
</head>
<body>
  <section class="business-card">
    <h1 class="company-name">Harlow Ridge Motors</h1>

    <ul class="contact-list">
      <li class="contact-item address">
        <span class="contact-icon">
          <svg width="20" height="20" viewBox="0 0 20 20" aria-hidden="true">
            <path d="M10 2 L19 10 H16 V18 H12 V13 H8 V18 H4 V10 H1 Z" fill="#ffffff"/>
          </svg>
        </span>
        <span class="contact-text">
          <span>2875 Brambleford Eastlvd</span>
          <span>Dunmore, Ga 302</span>
        </span>
      </li>
      <li class="contact-item phone">
        <span class="contact-icon">
          <svg width="20" height="22" viewBox="0 0 20 22" aria-hidden="true">
            <rect x="5" y="2" width="10" height="18" rx="2" fill="none" stroke="#ffffff" stroke-width="1.6"/>
            <circle cx="10" cy="16.5" r="1" fill="#ffffff"/>
          </svg>
        </span>
        <span class="contact-text">555,204,6170</span>
      </li>
    </ul>

    <div class="compass-art" role="img" aria-label="Silver compass rose star without direction letters"></div>
    <div class="car-photo" role="img" aria-label="Photo of a silver coupe, front three-quarter view"></div>

    <p class="services-tagline">SALES SERVICES REPAIR</p>
  </section>
</body>
</html>
```